Premium Personal Brand — Facebook Banner (Used Across All Platforms)

Update — Additional Color Direction
In addition to the dark charcoal/slate direction already described, I'm also interested in seeing variants with:
Dark navy blue — Deep, authoritative, intelligence-community feel. Same textured/matte treatment, not flat or bright.
Warm charcoal with steel blue accent — Keep the dark base but introduce a subtle steel blue gradient, accent line, or tonal shift. Sophisticated, modern, adds dimension without adding color noise.
Both should maintain the same premium, restrained, architectural feel described in the original brief. No bright blues, no corporate PowerPoint energy — think midnight, think depth, think weight.
Everything else in the brief remains the same.
I am building a premium personal brand as an executive advisor to founders ($5M+ revenue).
This contest is Facebook-banner–focused, but the design must represent a visual system that will be reused across:
- LinkedIn
- YouTube
I- nstagram
- X (Twitter)
- Website hero sections and other brand touchpoints
Think of the Facebook banner as the primary expression of the brand — not a one-off graphic.
This project is about discovering a high-end visual style and brand feel, not decoration.
What to design
Please submit one cohesive visual system, shown primarily as:
- Facebook banner (primary focus)
The same design language should clearly translate to all platforms listed above.
Designers are responsible for using the current recommended dimensions for each platform.
Quick clarification on background direction:
Backgrounds should have depth and texture, not flat color fields. Avoid pure white, light grey, or solid black backgrounds. Think matte, architectural materials — stone, graphite, concrete, steel — not blank canvases. Subtle tonal variation is encouraged. Obvious gradients or decorative patterns are not.
Text to use
Primary Headline:
- Your Business Is Too Valuable To Be Run On Hope.
Subheadline:
- You didn’t build a business to become its prisoner.
Name:
Milo Verant
The headline should be the dominant visual element.
Logo note (important)
My personal logo is currently being finalized.
For this contest:
- Use a simple “MV” monogram placeholder
- Clean, bold, geometric sans-serif
- Do not design a logo
- The winning design must allow an easy logo swap later.
Headshot note (important)
- Please do not include a headshot in the banner design.
- Most platforms display a circular profile image separately.
- The banner should stand on its own using typography, layout, and tone only.
- Design the banner assuming the profile photo will sit nearby, not inside the banner.
Style direction
The design should feel:
- Premium
- Calm
- Confident
- Restrained
- High-trust
- Dark, neutral backgrounds are preferred.
- Fewer elements are better than more.
Think:
- Owner-level advisor
- Private equity / boardroom tone
- Industrial, Modern, Minimalist, Elite, Architectural, not decorative
What to avoid
Please do not submit designs that feel:
- Promotional, hype-driven, or salesy
- Like a coach, guru, or agency
- Bright, colorful, or gradient-heavy
- Busy or over-designed
- Based on stock photos
- No motivational speaker energy.
Reaction test
- If someone sees this banner on Facebook (or later on LinkedIn, YouTube, etc.), the reaction should be:
“That person is serious. I’d trust them with important decisions.”
Final note
- I am not looking for many variations.
- I am looking for one strong visual direction you believe in.
Simple beats clever.
- Restraint beats decoration.

```html
<!DOCTYPE html>
<html lang="en">
<head>
<meta charset="utf-8">
<title>Milo Verant — Banner</title>
<link rel="stylesheet" href="https://fonts.googleapis.com/css2?family=Libre+Caslon+Text:wght@400&family=Poppins:wght@400;600&display=swap">
<style>
  :root {
    --stage: #e4e5e8;
    --navy-deep: #050b1c;
    --navy-mid: #0b1a3f;
    --navy-glow: #14306e;
    --panel: rgba(40, 62, 110, 0.55);
    --panel-edge: rgba(70, 110, 190, 0.55);
    --ink-light: #f3f4f7;
    --ink-soft: #dfe3ec;
    --monogram-fill: #0d0f14;
  }
  * { margin: 0; padding: 0; box-sizing: border-box; }
  html, body {
    width: 1200px;
    height: 690px;
    overflow: hidden;
    background: var(--stage);
  }
  .banner {
    position: absolute;
    left: 30px;
    top: 115px;
    width: 1140px;
    height: 459px;
    border-radius: 8px;
    overflow: hidden;
    background:
      radial-gradient(ellipse 55% 70% at 50% 55%, var(--navy-glow) 0%, transparent 70%),
      radial-gradient(ellipse 40% 50% at 20% 100%, rgba(20, 48, 110, 0.6) 0%, transparent 70%),
      radial-gradient(ellipse 35% 60% at 95% 30%, rgba(4, 8, 20, 0.7) 0%, transparent 75%),
      linear-gradient(180deg, var(--navy-mid) 0%, var(--navy-deep) 100%);
  }
  .monogram {
    position: absolute;
    left: 63px;
    top: 23px;
    width: 47px;
    height: 47px;
    border: 1px solid rgba(255, 255, 255, 0.55);
    border-radius: 2px;
    background: var(--monogram-fill);
    color: var(--ink-light);
    font-family: "Poppins", sans-serif;
    font-weight: 600;
    font-size: 22px;
    line-height: 47px;
    text-align: center;
  }
  .message-panel {
    position: absolute;
    left: 183px;
    top: 149px;
    width: 600px;
    height: 183px;
    border-radius: 10px;
    background: var(--panel);
    border: 1px solid var(--panel-edge);
    box-shadow: 0 0 18px rgba(40, 90, 200, 0.35);
  }
  .headline {
    position: absolute;
    left: 201px;
    top: 166px;
    font-family: "Libre Caslon Text", serif;
    font-weight: 400;
    font-size: 41px;
    line-height: 49px;
    color: var(--ink-light);
    letter-spacing: -0.3px;
  }
  .divider {
    position: absolute;
    left: 203px;
    top: 279px;
    width: 44px;
    height: 1px;
    background: var(--ink-soft);
  }
  .subheadline {
    position: absolute;
    left: 202px;
    top: 290px;
    font-family: "Poppins", sans-serif;
    font-size: 15.5px;
    color: var(--ink-soft);
  }
</style>
</head>
<body>
  <div class="banner">
    <div class="monogram">MV</div>
    <div class="message-panel"></div>
    <h1 class="headline">Your Business Is Too Valuable<br>To Be Run On Hope.</h1>
    <div class="divider"></div>
    <p class="subheadline">You didn’t build a business to become its prisoner.</p>
  </div>
</body>
</html>
```